Trip-Hop Instrumental Album from Producer Dario Welk needs a Front/Back Cover Design!

I need a CD cover design for the front and back of an instrumental hip-hop album that I've composed (so that I could print CD's or vinyls if I want to). The title of the album is Marrow Tide, and the artist name is Dario Welk. I'd like just the name of the album and the artist name on the front, and then the tracklisting on the back. The album is a collection of trippy hip-hop instrumentals, and the tracklisting is as follows:

Quiet on Halden
Glass Ember
Rust and Hollow
Slow Hymn for the Harbour
Pale Lantern
Gravelin
Wake Me Slow
Korvath

Here's a couple of the tracks that I put up, just to help you catch the vibe, if that helps.
https://tunebarrow.example/dariowelk/korvath-instrumental
https://tunebarrow.example/dariowelk/quiet-on-halden-instrumental
https://tunebarrow.example/dariowelk/rust-and-hollow-instrumental-1

Here's a few examples of some cover art that caught my eye. I don't want a carbon copy of these covers, but I absolutely love the atmosphere and the vibe that they create - smoky, etheral, trippy/glitchy yet weirdly beautiful, that kind of stuff generally. Just a general idea of the mood I'm looking for coverwise. I've also attached a couple photos of myself (one from the front, one from the side) so that if you decide you wanted to work a drawing of that into the front cover or the back cover you have that option if that's the vibe you're feeling. I'm trying to give you as much information as possible so that this process is easy, I hope the info I've given you is adequate. Overall I'm just looking for a cover/rear cover that will best accompany the music I've made, and I trust you will be able to help me achieve this.

Some examples of covers that I really like the atmosphere of (they're all pretty different so it might be worth taking a look at them):
Example 1: https://www.vidplume.example/watch?v=7tkaRMWepLoQ
Example 2: https://www.vidplume.example/watch?v=hQz-pwK8nbe&list=PL7rTMQ_2xbHc4gfkeWsLJAm3DqPodZt&index=105
Example 3: https://www.vidplume.example/watch?v=9-hDRtKxwmo&index=22&list=FLBz_tqW4_cuN3Rh8kdoaTVe
Example 4: https://www.vidplume.example/watch?v=eyT4LPQm7zk

If you need any more information, please contact me at dariowelk@mailrook.example and I'll be happy to give you any more information you'd like. Thank you very much.

Requirements
Must have
• Lo-fi, retro feel, doesn't look like a word-art collage. Preferably the album name/artist name in smallish writing (some jagged font) so that the main focus is whatever the main image on the cover is. Also I'd prefer it if there were just one image on the front cover, which takes up the whole cover, and then the artist name/album title on the front but not very large so that the main focus is whatever the image is. Again, lo-fi, dark, atmospheric, trippy is the way to go. Please no images of people. If you want to see some examples of covers that I liked check the project description because there are links in there to some covers that I liked.

```html
<!DOCTYPE html>
<html lang="en">
<head>
<meta charset="utf-8">
<title>Dario Welk — Marrow Tide — Back Cover</title>
<link rel="stylesheet" href="https://fonts.googleapis.com/css2?family=Indie+Flower&display=swap">
<style>
  :root {
    --page-bg: #d9d9db;
    --cover-deep: #17130e;
    --cover-night: #1f1a1c;
    --cover-violet: #2b2230;
    --cover-olive: #3b3818;
    --cover-moss: #4d4a1c;
    --cover-umber: #5e4512;
    --cover-ember: #7a5a14;
    --cover-straw: #b9a772;
    --track-ink: #ffffff;
  }
  * { box-sizing: border-box; margin: 0; padding: 0; }
  html, body {
    width: 1200px;
    height: 900px;
    overflow: hidden;
    background: var(--page-bg);
  }
  .back-cover {
    position: absolute;
    left: 110px;
    top: 60px;
    width: 980px;
    height: 780px;
    overflow: hidden;
    background: var(--cover-deep);
  }
  .back-cover__artwork {
    position: absolute;
    inset: 0;
    background:
      radial-gradient(ellipse 9% 22% at 50% 10%, rgba(120,118,40,0.75) 0%, transparent 100%),
      radial-gradient(ellipse 14% 30% at 50% 55%, rgba(122,90,20,0.55) 0%, transparent 100%),
      radial-gradient(ellipse 16% 40% at 50% 85%, rgba(94,69,18,0.55) 0%, transparent 100%),
      radial-gradient(ellipse 10% 34% at 13% 30%, rgba(185,167,114,0.38) 0%, transparent 100%),
      radial-gradient(ellipse 10% 34% at 87% 30%, rgba(185,167,114,0.38) 0%, transparent 100%),
      radial-gradient(ellipse 9% 30% at 20% 78%, rgba(185,167,114,0.30) 0%, transparent 100%),
      radial-gradient(ellipse 9% 30% at 80% 78%, rgba(185,167,114,0.30) 0%, transparent 100%),
      radial-gradient(ellipse 20% 40% at 33% 40%, rgba(77,74,28,0.55) 0%, transparent 100%),
      radial-gradient(ellipse 20% 40% at 67% 40%, rgba(77,74,28,0.55) 0%, transparent 100%),
      linear-gradient(180deg, rgba(0,0,0,0) 55%, rgba(40,34,14,0.5) 100%),
      linear-gradient(90deg,
        var(--cover-violet) 0%,
        var(--cover-night) 14%,
        var(--cover-olive) 30%,
        var(--cover-deep) 40%,
        var(--cover-umber) 50%,
        var(--cover-deep) 60%,
        var(--cover-olive) 70%,
        var(--cover-night) 86%,
        var(--cover-violet) 100%);
  }
  .tracklist {
    position: absolute;
    left: 50%;
    top: 56px;
    transform: translateX(-50%);
    width: 520px;
    list-style: none;
    text-align: center;
    font-family: "Indie Flower", cursive;
    font-size: 52px;
    line-height: 74px;
    color: var(--track-ink);
  }
</style>
</head>
<body>
  <main class="back-cover">
    <div class="back-cover__artwork" role="img" aria-label="Mirrored dark forest path with glowing golden branch-like lightning streaks on both sides and a pale outline down the centre"></div>
    <ol class="tracklist">
      <li class="tracklist__item">Quiet on Halden</li>
      <li class="tracklist__item">Glass Ember</li>
      <li class="tracklist__item">Rust and Hollow</li>
      <li class="tracklist__item">Slow Hymn for the Harbour</li>
      <li class="tracklist__item">Pale Lantern</li>
      <li class="tracklist__item">Gravelin</li>
      <li class="tracklist__item">Wake Me Slow</li>
      <li class="tracklist__item">Korvath</li>
    </ol>
  </main>
</body>
</html>
```